New modern business card design

To design a brand new business card that's clean & modern in terms of layout.
I have attached our company logo and also basic information regarding what is needed on the card that also needs to be editable.

Target Market(s)

motor trade

Contact Information for Business Card

logo, name, title, tel, mob, email, address, www, all information is in the word.doc file

Requirements
Must have
• white background
Nice to have
• Nice clean font

```html
<!DOCTYPE html>
<html lang="en">
<head>
<meta charset="utf-8">
<title>Bolt Draw Ltd – Business Card</title>
<link href="https://fonts.googleapis.com/css2?family=Michroma&family=Arimo:wght@400;700&display=swap" rel="stylesheet">
<style>
  :root {
    --stage: #2c2c2e;
    --brand-blue: #2a78c2;
    --brand-blue-light: #3b8ad3;
    --brand-grey: #9a9ea3;
    --paper: #ffffff;
    --ink-light: #ffffff;
  }
  * { margin: 0; padding: 0; box-sizing: border-box; }
  html, body { width: 1200px; height: 902px; overflow: hidden; }
  body {
    background: var(--stage);
    font-family: "Arimo", Arial, sans-serif;
    position: relative;
  }
  .card {
    position: absolute;
    width: 700px;
    height: 400px;
    border-radius: 28px;
    overflow: hidden;
    box-shadow: 0 14px 30px rgba(0,0,0,0.45);
  }
  /* Back side */
  .card-back {
    left: 60px;
    top: 40px;
    background: var(--brand-blue);
  }
  .card-back .pattern-area {
    position: absolute;
    inset: 0;
    background: linear-gradient(135deg, var(--brand-blue) 0%, var(--brand-blue-light) 55%, var(--brand-blue) 100%);
  }
  .card-back .back-name {
    position: absolute;
    right: 48px;
    top: 170px;
    font-family: "Michroma", "Arial Black", sans-serif;
    font-size: 26px;
    color: var(--ink-light);
    letter-spacing: 1px;
  }
  /* Front side */
  .card-front {
    left: 440px;
    top: 462px;
    background: var(--paper);
    display: flex;
  }
  .brand-panel {
    width: 48%;
    display: flex;
    flex-direction: column;
    align-items: center;
    justify-content: center;
    padding-top: 20px;
  }
  .brand-name {
    font-family: "Michroma", "Arial Black", sans-serif;
    font-size: 30px;
    color: var(--brand-blue);
    letter-spacing: 1px;
    white-space: nowrap;
  }
  .brand-rule {
    width: 270px;
    height: 2px;
    background: var(--brand-blue);
    margin: 8px 0 6px;
  }
  .brand-suffix {
    font-family: "Michroma", "Arial Black", sans-serif;
    font-size: 15px;
    color: var(--brand-grey);
    letter-spacing: 10px;
    padding-left: 10px;
  }
  .info-panel {
    width: 52%;
    background: var(--brand-blue);
    color: var(--ink-light);
    padding: 44px 34px 34px 30px;
    display: flex;
    flex-direction: column;
    justify-content: space-between;
    text-align: right;
  }
  .person-name {
    font-family: "Michroma", "Arial Black", sans-serif;
    font-size: 21px;
    letter-spacing: 1px;
    line-height: 1.1;
  }
  .person-title {
    font-family: "Michroma", "Arial Black", sans-serif;
    font-size: 13px;
    letter-spacing: 1px;
    margin-top: 4px;
  }
  .info-rule {
    height: 1px;
    background: var(--ink-light);
    margin: 12px 0 10px;
  }
  .address {
    font-size: 15px;
    line-height: 1.35;
  }
  .contacts {
    font-size: 17px;
    line-height: 1.5;
  }
  .contact-row {
    display: flex;
    justify-content: flex-end;
    align-items: center;
    gap: 10px;
  }
  .contact-icon {
    width: 20px;
    height: 20px;
    flex: none;
  }
  .contact-row.email { margin-top: 6px; padding-right: 30px; }
</style>
</head>
<body>

<section class="card card-back" aria-label="Business card, back side">
  <div class="pattern-area" role="img" aria-label="Repeating brand monogram pattern in tonal blue"></div>
  <div class="back-name">BOLT DRAW</div>
</section>

<section class="card card-front" aria-label="Business card, front side">
  <div class="brand-panel">
    <div class="brand-name">BOLT DRAW</div>
    <div class="brand-rule"></div>
    <div class="brand-suffix">LTD</div>
  </div>

  <div class="info-panel">
    <div class="identity">
      <div class="person-name">DANIEL HARPER</div>
      <div class="person-title">GENERAL MANAGER</div>
      <div class="info-rule"></div>
      <div class="address">
        Kestrel Road<br>
        Denton, Northfield<br>
        NF4 2QT<br>
        www.bolt-draw.co.uk
      </div>
    </div>

    <div class="contacts">
      <div class="contact-row phone">
        <span>0161 555 0142</span>
        <svg class="contact-icon" viewBox="0 0 20 20" aria-hidden="true">
          <circle cx="10" cy="10" r="10" fill="#fff"/>
          <path d="M6.5 5.5l2 0 1 2.5-1.2 1a6 6 0 0 0 2.7 2.7l1-1.2 2.5 1v2c-4.5.5-8.5-3.5-8-8z" fill="var(--brand-blue)"/>
        </svg>
      </div>
      <div class="contact-row mobile">
        <span>07700 900 318</span>
        <svg class="contact-icon" viewBox="0 0 20 20" aria-hidden="true">
          <circle cx="10" cy="10" r="10" fill="#fff"/>
          <rect x="7" y="4.5" width="6" height="11" rx="1" fill="none" stroke="var(--brand-blue)" stroke-width="1.4"/>
          <circle cx="10" cy="13.5" r="0.7" fill="var(--brand-blue)"/>
        </svg>
      </div>
      <div class="contact-row mail">
        <span></span>
        <svg class="contact-icon" viewBox="0 0 20 20" aria-hidden="true">
          <circle cx="10" cy="10" r="10" fill="#fff"/>
          <rect x="5" y="6.5" width="10" height="7" fill="none" stroke="var(--brand-blue)" stroke-width="1.3"/>
          <path d="M5 6.5l5 4 5-4" fill="none" stroke="var(--brand-blue)" stroke-width="1.3"/>
        </svg>
      </div>
      <div class="contact-row email">
        <span>dharper@bolt-draw.co.uk</span>
      </div>
    </div>
  </div>
</section>

</body>
</html>
```